Driving-coach/trainer who wants to inform about the offer and how I can help people to drive more re

I need a flyer that informs potential customers about my offer.

DL size 210 mm x 99 mm, vertical!

I'm a trainer/coach who helps people to drive a car more relaxed, without fear and more confident.

It's a one to one training. I do train people in their own car. It gets people their freedom back to go where and when they like to go by own car...

Target Market(s)

People (man an woman) who are afraid of driving a car, or are very stressed while driving....

Industry/Entity Type

Life Coaching

Font styles to use
Sans Serif

Colors
acd136

Requirements
Must have
• Page 1:
• -my offer (see text-pdf)
• -three fotos (see attached files "Pixmarra") of people who are satisfied with my offer
• Page 2:
• -advantages in the work with me.
• -contact information
• -and a picture of me (see attached file) next to the contact information or the advantages of my work
• -my logo (see attached file) on Page 1 + 2
• -i like a "clear" and structured layout. "Less is more"

```html
<!DOCTYPE html>
<html lang="de">
<head>
<meta charset="utf-8">
<title>Fahrangst-Coach – Flyer</title>
<link rel="stylesheet" href="https://fonts.googleapis.com/css2?family=Roboto+Condensed:wght@400;700&family=Roboto+Slab:wght@300;400;700&display=swap">
<style>
  :root{
    --lime:#acd136;
    --green:#5c9a3a;
    --green-dark:#3f7a2c;
    --green-mid:#4c8a33;
    --grey-dark:#5a5a5a;
    --grey-mid:#7b7b7b;
    --grey-light:#c9c9c9;
    --white:#ffffff;
    --ink:#1a1a1a;
    --ink-green:#1f3d16;
  }
  *{margin:0;padding:0;box-sizing:border-box}
  html,body{width:1200px;height:2778px;overflow:hidden;background:var(--white)}
  .flyer{position:relative;width:1200px;height:2778px;overflow:hidden;background:var(--white);font-family:"Roboto Condensed",Arial,sans-serif}

  /* Header band */
  .steps-header{position:absolute;left:0;top:41px;width:1200px;height:196px}
  .steps-header svg{position:absolute;inset:0}
  .steps-header .kicker{position:absolute;left:269px;top:18px;font-family:"Roboto Slab",Georgia,serif;font-weight:400;font-size:42px;line-height:1.2;color:var(--white)}
  .steps-header h1{position:absolute;left:269px;top:86px;font-family:"Roboto Slab",Georgia,serif;font-weight:700;font-size:60px;line-height:1.2;color:var(--white);letter-spacing:1px}

  /* Steps */
  .step{position:absolute;width:334px;height:334px;border-radius:50%;background:var(--lime);display:flex;align-items:center;justify-content:center;text-align:center;color:var(--white);font-weight:700;font-size:40px;line-height:1.25;padding:0 20px}
  .step-1{left:55px;top:314px}
  .step-2{left:437px;top:314px;padding-top:36px}
  .step-3{left:818px;top:314px;padding-top:30px}
  .step-num{position:absolute;width:116px;height:116px;border-radius:50%;background:var(--green-dark);color:var(--white);font-weight:700;font-size:78px;display:flex;align-items:center;justify-content:center}
  .num-1{left:72px;top:290px}
  .num-2{left:453px;top:290px}
  .num-3{left:834px;top:290px}
  .step-note{position:absolute;left:728px;top:680px;width:450px;text-align:center;font-size:25px;line-height:1.3;color:var(--ink)}

  /* Advantages panel */
  .advantages-bg{position:absolute;left:0;top:700px;width:1200px;height:932px}
  .advantages{position:absolute;left:0;top:890px;width:1200px;color:var(--white);font-family:"Roboto Slab",Georgia,serif}
  .advantages h2{margin-left:50px;font-weight:700;font-size:42px;line-height:1.2;letter-spacing:.5px}
  .advantages ul{list-style:none;margin-top:22px}
  .advantages li{position:relative;padding-left:96px;padding-right:70px;font-weight:300;font-size:37px;line-height:48px;margin-bottom:14px}
  .advantages li::before{content:"";position:absolute;left:54px;top:12px;width:0;height:0;border-left:24px solid transparent;border-bottom:24px solid var(--white)}
  .advantages li.narrow{padding-right:430px}

  /* Contact band */
  .contact{position:absolute;left:0;top:1630px;width:1200px;height:453px;background:var(--green)}
  .contact .name{position:absolute;left:48px;top:60px;font-weight:700;font-size:58px;line-height:1.2;color:var(--white)}
  .contact .label{position:absolute;left:48px;font-size:34px;line-height:1.2;color:var(--ink-green)}
  .contact .value{position:absolute;left:48px;font-size:50px;line-height:1.2;color:var(--white)}
  .label-phone{top:175px}
  .value-phone{top:218px}
  .label-web{top:308px}
  .value-web{top:348px}
  .portrait{position:absolute;left:744px;top:1535px;width:432px;height:432px;border-radius:50%;border:8px solid var(--white);background:radial-gradient(circle at 50% 40%,#f2f2f2,#d9d9d9 70%,#c7c7c7);box-shadow:0 2px 8px rgba(0,0,0,.25)}

  /* Brand name */
  .brand{position:absolute;left:62px;top:2140px;display:flex;align-items:center;gap:22px}
  .brand-dot{width:44px;height:44px;border-radius:50%;background:var(--green)}
  .brand-name{font-family:"Roboto Condensed",Arial,sans-serif;font-weight:700;font-size:56px;line-height:1;color:var(--green)}

  /* Photo area */
  .hero-photo{position:absolute;left:0;top:2263px;width:1200px;height:515px;background:linear-gradient(100deg,#6b5a44 0%,#a97a4c 30%,#d9c9b2 55%,#8f8a83 75%,#c98a4a 100%)}
</style>
</head>
<body>
<main class="flyer">

  <header class="steps-header">
    <svg width="1200" height="196" viewBox="0 0 1200 196" aria-hidden="true">
      <rect x="0" y="0" width="1200" height="196" fill="var(--green)"/>
      <polygon points="0,0 150,0 250,98 150,196 0,196 100,98" fill="var(--green-dark)"/>
      <polygon points="130,0 200,0 300,98 200,196 130,196 230,98" fill="var(--green-mid)"/>
    </svg>
    <p class="kicker">Das muss nicht so bleiben!</p>
    <h1>3 Schritte zur Lösung:</h1>
  </header>

  <section class="steps">
    <div class="step step-1">Erstgespräch<br>vereinbaren</div>
    <div class="step step-2">Analyse<br>Ihrer individuellen<br>Situation und<br>Zielsetzung</div>
    <div class="step step-3">Individuelles<br>Coaching und<br>Training</div>
    <span class="step-num num-1">1</span>
    <span class="step-num num-2">2</span>
    <span class="step-num num-3">3</span>
    <p class="step-note">(ggf. Fahrangst-Therapie - als psychotherapeutische Heilpraktikerin bin ich auf Angst- und Panikstörungen spezialisiert)</p>
  </section>

  <svg class="advantages-bg" width="1200" height="932" viewBox="0 0 1200 932" aria-hidden="true">
    <defs>
      <linearGradient id="panelGrey" x1="0" y1="0" x2="0" y2="1">
        <stop offset="0" stop-color="#5a5a5a"/>
        <stop offset=".5" stop-color="#7b7b7b"/>
        <stop offset="1" stop-color="#5a5a5a"/>
      </linearGradient>
      <linearGradient id="edgeGrey" x1="0" y1="0" x2="1" y2="0">
        <stop offset="0" stop-color="#9a9a9a"/>
        <stop offset="1" stop-color="#c9c9c9"/>
      </linearGradient>
    </defs>
    <polygon points="0,0 1200,168 1200,190 0,40" fill="url(#edgeGrey)"/>
    <polygon points="0,40 1200,190 1200,932 0,932" fill="url(#panelGrey)"/>
  </svg>

  <section class="advantages">
    <h2>Vorteile bei der Arbeit mit mir:</h2>
    <ul>
      <li>über 10 Jahre Erfahrung als Trainerin und Coach im Bereich Fahrsicherheit.</li>
      <li>Als psychotherapeutische Heilpraktikerin bin ich auf Angststörungen und Panikattacken spezialisiert</li>
      <li>100 % auf Sie zugeschnitten: ich hole Sie genau dort ab, wo Sie jetzt stehen und unterstütze Sie in Ihrem Prozess individuell und zielführend.</li>
      <li>Wenn es Ihnen nicht möglich ist, in meine Praxis nach Lindenau Westhof zu kommen: Mit der mobilen Praxis komme ich auch zu Ihnen.</li>
      <li class="narrow">Termine sind auch abends und am Wochenende möglich.</li>
    </ul>
  </section>

  <section class="contact">
    <p class="name">Katrin Lindqvist</p>
    <p class="label label-phone">Oder rufen Sie mich einfach an:</p>
    <p class="value value-phone">Tel. 0151 48 36 17 92</p>
    <p class="label label-web">Weitere Informationen finden Sie auf:</p>
    <p class="value value-web">www.fahrangst-gelassen-coach.de</p>
  </section>
  <div class="portrait" role="img" aria-label="Porträtfoto der Trainerin in weißer Bluse vor hellem Hintergrund"></div>

  <div class="brand">
    <span class="brand-dot" aria-hidden="true"></span>
    <span class="brand-name">Lindqvist Fahrcoaching</span>
  </div>

  <div class="hero-photo" role="img" aria-label="Foto einer lächelnden Frau am Steuer eines offenen Cabrios mit hellbraunen Ledersitzen"></div>

</main>
</body>
</html>
```